Maple Burrow Canine Massage Needs a Business Card Design

Maple Burrow Canine Massage is a new therapeutic canine massage company located in Nederland, Colorado. I need a business card design that include my logo and basic contact information.

Target Market(s)

Pet owners, veterinarians

Industry/Entity Type

Business

Contact Information for Business Card

Tessa Lindqvist, CCMT
303.581.7296
tessa@mapleburrowmassage.example
www.mapleburrowmassage.example

Colors
6c459b
886aae
b8a6cd
a64599
b768aa
d3a5cc
fbed22

Requirements
Must have
• Font should be similar to font in logo.

```html
<!DOCTYPE html>
<html lang="en">
<head>
<meta charset="utf-8">
<title>Maple Burrow Canine Massage – Business Card</title>
<link href="https://fonts.googleapis.com/css2?family=Open+Sans:wght@400;600&display=swap" rel="stylesheet">
<style>
  :root {
    --purple-deep: #6c459b;
    --purple-mid: #886aae;
    --lavender: #b98fc9;
    --lavender-light: #cfa9dc;
    --gold: #e6c13a;
    --ink: #5a4a66;
    --paper: #ffffff;
    --stage: #ece8ef;
  }
  * { box-sizing: border-box; margin: 0; padding: 0; }
  html, body {
    width: 1200px; height: 843px; overflow: hidden;
    background: var(--stage);
    font-family: "Open Sans", Arial, sans-serif;
  }
  .sheet {
    width: 1200px; height: 843px;
    display: flex; align-items: center; justify-content: center; gap: 40px;
  }
  .card {
    position: relative;
    width: 540px; height: 309px;
    border-radius: 18px;
    overflow: hidden;
    box-shadow: 0 10px 28px rgba(60, 40, 80, 0.22);
  }

  /* Back side */
  .card-back {
    background: linear-gradient(135deg, var(--lavender-light) 0%, var(--lavender) 100%);
  }
  .back-artwork {
    position: absolute; left: 30px; top: 40px;
    width: 300px; height: 230px;
    border-radius: 12px;
    background: linear-gradient(160deg, rgba(108,69,155,0.55), rgba(108,69,155,0.25));
  }
  .back-wordmark {
    position: absolute; right: 34px; top: 150px;
    width: 170px;
    color: var(--gold);
    font-weight: 600; font-size: 20px; line-height: 1.25;
    letter-spacing: 1px; text-transform: uppercase; text-align: right;
  }

  /* Front side */
  .card-front { background: var(--paper); }
  .front-disc { position: absolute; inset: 0; }
  .contact {
    position: absolute; left: 36px; top: 104px;
    color: var(--ink);
  }
  .contact-name {
    font-size: 21px; font-weight: 600; color: var(--purple-deep);
    margin-bottom: 10px;
  }
  .contact-name .credential { font-size: 15px; font-weight: 400; }
  .contact-line {
    display: flex; align-items: center; gap: 8px;
    font-size: 14px; line-height: 24px;
  }
  .contact-line svg { width: 13px; height: 13px; flex: none; }
  .brand-block {
    position: absolute; right: 40px; top: 66px;
    width: 150px;
    display: flex; flex-direction: column; align-items: center; gap: 12px;
  }
  .brand-dot {
    width: 96px; height: 96px; border-radius: 50%;
    background: var(--purple-mid);
  }
  .brand-name {
    color: var(--purple-deep);
    font-weight: 600; font-size: 15px; line-height: 1.3;
    letter-spacing: 1px; text-transform: uppercase; text-align: center;
  }
</style>
</head>
<body>
<main class="sheet">

  <section class="card card-back">
    <div class="back-artwork" role="img" aria-label="Large brand illustration area on the card back"></div>
    <div class="back-wordmark">Maple Burrow Canine Massage</div>
  </section>

  <section class="card card-front">
    <svg class="front-disc" viewBox="0 0 540 309" aria-hidden="true">
      <defs>
        <linearGradient id="discFill" x1="0" y1="0" x2="1" y2="1">
          <stop offset="0" stop-color="#c79dd6"/>
          <stop offset="1" stop-color="#b07fc2"/>
        </linearGradient>
      </defs>
      <circle cx="105" cy="215" r="214" fill="none" stroke="var(--gold)" stroke-width="4"/>
      <circle cx="105" cy="215" r="207" fill="url(#discFill)"/>
    </svg>

    <div class="contact">
      <p class="contact-name">Tessa Lindqvist, <span class="credential">CCMT</span></p>
      <p class="contact-line">
        <svg viewBox="0 0 16 16"><path fill="var(--purple-deep)" d="M3.5 1l3 3-1.6 2.1a9 9 0 0 0 5 5L12 9.5l3 3-2 2.5C6.5 15 1 9.5 1 3z"/></svg>
        303.581.7296
      </p>
      <p class="contact-line">
        <svg viewBox="0 0 16 16"><rect x="1" y="3" width="14" height="10" rx="1.5" fill="var(--purple-deep)"/><path d="M2 4.5l6 4.5 6-4.5" fill="none" stroke="#fff" stroke-width="1.2"/></svg>
        tessa@mapleburrowmassage.example
      </p>
      <p class="contact-line">
        <svg viewBox="0 0 16 16"><circle cx="8" cy="8" r="6.5" fill="none" stroke="var(--purple-deep)" stroke-width="1.5"/><ellipse cx="8" cy="8" rx="2.8" ry="6.5" fill="none" stroke="var(--purple-deep)" stroke-width="1.2"/><path d="M1.5 8h13" stroke="var(--purple-deep)" stroke-width="1.2"/></svg>
        www.mapleburrowmassage.example
      </p>
    </div>

    <div class="brand-block">
      <div class="brand-dot"></div>
      <div class="brand-name">Maple Burrow Canine Massage</div>
    </div>
  </section>

</main>
</body>
</html>
```